Business card for event manager / organizer "velmora tandem"

Draft of a new valuable business card for my company.
Events, personnel service providers, festivals

```html
<!DOCTYPE html>
<html lang="de">
<head>
<meta charset="utf-8">
<title>velmora tandem – Visitenkarte</title>
<link href="https://fonts.googleapis.com/css2?family=Montserrat:ital,wght@0,700;1,800&family=Exo+2:wght@300;400&display=swap" rel="stylesheet">
<style>
  :root {
    --backdrop: #c9934a;
    --card-dark: #2b2b2e;
    --card-mid: #333338;
    --orange: #ee7a2b;
    --arc-gold: #e9a43a;
    --white: #ffffff;
    --muted: #b9b9bd;
    --photo-blue: #3b3f4c;
  }
  * { box-sizing: border-box; margin: 0; padding: 0; }
  html, body { width: 1200px; height: 1200px; overflow: hidden; }
  body { background: var(--backdrop); position: relative; font-family: "Exo 2", sans-serif; }

  .card {
    position: absolute; top: 253px; width: 425px; height: 693px;
    overflow: hidden; background: linear-gradient(180deg, var(--card-mid) 0%, var(--card-dark) 60%, #252527 100%);
  }
  .card--front { left: 114px; }
  .card--back { left: 660px; }

  .brand { position: absolute; display: flex; align-items: center; gap: 9px; }
  .brand__mark { background: var(--orange); flex: none; }
  .brand__name { font-family: "Montserrat", sans-serif; font-weight: 700; color: var(--white); white-space: nowrap; line-height: 1; }
  .brand__tagline { position: absolute; font-family: "Exo 2", sans-serif; font-weight: 300; color: var(--muted); white-space: nowrap; line-height: 1; }

  .card--front .brand { left: 98px; top: 40px; }
  .card--front .brand__mark { width: 34px; height: 34px; }
  .card--front .brand__name { font-size: 24px; }
  .card--front .brand__tagline { left: 150px; top: 108px; font-size: 9.5px; }

  .arc { position: absolute; left: 0; top: 0; width: 425px; height: 693px; }

  .portrait {
    position: absolute; left: 100px; top: 136px; width: 250px; height: 250px;
    background: radial-gradient(ellipse 55% 60% at 50% 55%, #6d6f78 0%, #4a4b53 45%, rgba(43,43,46,0) 100%);
  }

  .person-name {
    position: absolute; left: 0; width: 425px; text-align: center;
    font-family: "Montserrat", sans-serif; line-height: 1;
  }
  .person-name__first { top: 368px; font-size: 88px; font-weight: 800; font-style: italic; color: var(--white); letter-spacing: -1px; padding-left: 14px; }
  .person-name__last { top: 448px; font-size: 51px; font-weight: 700; color: var(--orange); padding-left: 10px; }

  .contacts { position: absolute; left: 62px; top: 518px; list-style: none; }
  .contacts li { display: flex; align-items: center; gap: 7px; height: 20.7px; font-size: 14px; font-weight: 300; color: #e6e6e8; white-space: nowrap; }
  .contacts svg { width: 11px; height: 11px; flex: none; }

  .event-photo {
    position: absolute; inset: 0;
    background:
      radial-gradient(ellipse 40% 50% at 80% 60%, rgba(150,140,130,0.35) 0%, rgba(59,63,76,0) 100%),
      radial-gradient(ellipse 35% 55% at 30% 55%, rgba(30,30,36,0.6) 0%, rgba(59,63,76,0) 100%),
      linear-gradient(180deg, #3f4351 0%, var(--photo-blue) 50%, #3a3a3f 100%);
  }
  .card--back .brand { left: 44px; top: 315px; gap: 12px; }
  .card--back .brand__mark { width: 44px; height: 44px; }
  .card--back .brand__name { font-size: 32px; }
  .card--back .brand__tagline { left: 126px; top: 396px; font-size: 13px; color: #d4d4d8; }
</style>
</head>
<body>

<section class="card card--front">
  <div class="brand">
    <span class="brand__mark"></span>
    <span class="brand__name">velmora tandem</span>
  </div>
  <p class="brand__tagline">…weil jedes Fest Profis verdient!</p>

  <svg class="arc" viewBox="0 0 425 693" aria-hidden="true">
    <defs>
      <linearGradient id="arcFade" x1="0" y1="245" x2="0" y2="440" gradientUnits="userSpaceOnUse">
        <stop offset="0" stop-color="#e9a43a" stop-opacity="1"/>
        <stop offset="0.6" stop-color="#e9a43a" stop-opacity="0.55"/>
        <stop offset="1" stop-color="#e9a43a" stop-opacity="0"/>
      </linearGradient>
      <linearGradient id="arcFadeInner" x1="0" y1="290" x2="0" y2="440" gradientUnits="userSpaceOnUse">
        <stop offset="0" stop-color="#9a8c78" stop-opacity="0.55"/>
        <stop offset="1" stop-color="#9a8c78" stop-opacity="0"/>
      </linearGradient>
    </defs>
    <circle cx="213" cy="458" r="203" fill="none" stroke="url(#arcFade)" stroke-width="18"/>
    <circle cx="213" cy="458" r="170" fill="none" stroke="url(#arcFadeInner)" stroke-width="10"/>
  </svg>

  <div class="portrait" role="img" aria-label="Porträtfoto des Eventmanagers in Weste und Hemd mit verschränkten Armen"></div>

  <h1 class="person-name person-name__first">JONAS</h1>
  <h2 class="person-name person-name__last">Verlinde</h2>

  <ul class="contacts">
    <li><svg viewBox="0 0 24 24"><path fill="#fff" d="M6.6 10.8a15 15 0 0 0 6.6 6.6l2.2-2.2c.3-.3.7-.4 1-.2 1.1.4 2.3.6 3.6.6.6 0 1 .4 1 1V20c0 .6-.4 1-1 1A17 17 0 0 1 3 4c0-.6.4-1 1-1h3.5c.6 0 1 .4 1 1 0 1.3.2 2.5.6 3.6.1.3 0 .7-.2 1z"/></svg>01234 567 89 01</li>
    <li><svg viewBox="0 0 24 24"><path fill="#fff" d="M6.6 10.8a15 15 0 0 0 6.6 6.6l2.2-2.2c.3-.3.7-.4 1-.2 1.1.4 2.3.6 3.6.6.6 0 1 .4 1 1V20c0 .6-.4 1-1 1A17 17 0 0 1 3 4c0-.6.4-1 1-1h3.5c.6 0 1 .4 1 1 0 1.3.2 2.5.6 3.6.1.3 0 .7-.2 1z"/></svg>0170 000 12 34</li>
    <li><svg viewBox="0 0 24 24" fill="none" stroke="#bbb" stroke-width="1.6"><circle cx="12" cy="12" r="9.5"/><ellipse cx="12" cy="12" rx="4" ry="9.5"/><path d="M2.5 12h19M4 7h16M4 17h16"/></svg>www.velmora-tandem.de</li>
    <li><svg viewBox="0 0 24 24" fill="none" stroke="#bbb" stroke-width="1.6"><rect x="2" y="5" width="20" height="14"/><path d="M2 5l10 8 10-8M2 19l7-7M22 19l-7-7"/></svg>info@velmora-tandem.de</li>
    <li><svg viewBox="0 0 24 24" fill="none" stroke="#fff" stroke-width="1.8"><path d="M12 22s-7-7.5-7-12a7 7 0 0 1 14 0c0 4.5-7 12-7 12z"/><circle cx="12" cy="10" r="2.5"/></svg>Lindenweg 12, 10115 Musterstadt</li>
    <li><svg viewBox="0 0 24 24"><circle cx="12" cy="12" r="11" fill="#fff"/></svg>www.social-page.de/velmoratandem</li>
  </ul>
</section>

<section class="card card--back">
  <div class="event-photo" role="img" aria-label="Gedimmtes Foto eines Brautpaares, das im Konfettiregen tanzt"></div>
  <div class="brand">
    <span class="brand__mark"></span>
    <span class="brand__name">velmora tandem</span>
  </div>
  <p class="brand__tagline">…weil jedes Fest Profis verdient!</p>
</section>

</body>
</html>
```